MIRVEL soap beauty bar

I need a box designed to put a 4oz bar of soap inside. All sides of the box need design. A refreshingly fragrant blend of citrus and spicy notes, it is made with a blend of essential oils including ginger, mandarin, lemon and orange flowers

Target Market(s)

Homeless people

Requirements
Must have
• My company logo as pictured with text and design like a standard bar of soap. Weight 4oz, ingredients:
Olive oil, Coconut oil,Organic sustainable palm oil,Water,Lye,Shea butter, orange, ginger, mandarin, lemon essential oil. uploading pics for inspiration.
Nice to have
• The soap box measurements are Dimensions (L x W x H). 5.75 x 3.80 x 5.60 Inches ...

```html
<!DOCTYPE html>
<html lang="en">
<head>
<meta charset="utf-8">
<title>MIRVEL Soap – Box Panels</title>
<link href="https://fonts.googleapis.com/css2?family=Quicksand:wght@300;700&display=swap" rel="stylesheet">
<style>
  :root {
    --page-bg: #f3f3f1;
    --lid-white: #ececec;
    --leaf-green: #5fa845;
    --soft-green: #8cc36c;
    --lemon: #e6e23a;
    --pale-yellow: #f1ec7a;
    --brand-green: #2f8a3c;
    --brand-red: #d8262f;
    --type-green: #86c46f;
    --fold-line: rgba(0, 0, 0, 0.12);
  }
  html, body {
    margin: 0;
    padding: 0;
    width: 1200px;
    height: 1000px;
    overflow: hidden;
    background: var(--page-bg);
  }
  .box-net {
    position: absolute;
    left: 110px;
    top: 70px;
    width: 1000px;
    height: 860px;
  }
  .box-net__art {
    position: absolute;
    inset: 0;
    width: 100%;
    height: 100%;
    display: block;
  }
  .lid-type {
    position: absolute;
    left: 0;
    top: 0;
    width: 860px;
    height: 640px;
  }
  .brand {
    position: absolute;
    left: 250px;
    top: 150px;
    display: flex;
    align-items: center;
    gap: 10px;
    font-family: "Quicksand", sans-serif;
    font-weight: 700;
    font-size: 34px;
    line-height: 1;
    letter-spacing: 1px;
    color: var(--brand-green);
  }
  .brand__dot {
    width: 28px;
    height: 28px;
    border-radius: 50%;
    background: var(--brand-red);
  }
  .product-name {
    position: absolute;
    left: 0;
    right: 0;
    top: 225px;
    margin: 0;
    text-align: center;
    font-family: "Quicksand", sans-serif;
    font-weight: 300;
    font-size: 160px;
    line-height: 1;
    letter-spacing: 2px;
    color: var(--type-green);
  }
  .product-weight {
    position: absolute;
    left: 430px;
    top: 392px;
    font-family: "Quicksand", sans-serif;
    font-weight: 300;
    font-size: 26px;
    line-height: 1;
    color: var(--type-green);
  }
</style>
</head>
<body>
  <section class="box-net">
    <svg class="box-net__art" viewBox="0 0 1000 860" xmlns="http://www.w3.org/2000/svg">
      <defs>
        <linearGradient id="citrus-swirl" x1="0" y1="0" x2="1" y2="1">
          <stop offset="0" stop-color="#6fb24f"/>
          <stop offset="0.2" stop-color="#e6e23a"/>
          <stop offset="0.4" stop-color="#f1ec7a"/>
          <stop offset="0.6" stop-color="#8cc36c"/>
          <stop offset="0.8" stop-color="#e6e23a"/>
          <stop offset="1" stop-color="#5fa845"/>
        </linearGradient>
        <linearGradient id="side-swirl" x1="0" y1="0" x2="1" y2="1">
          <stop offset="0" stop-color="#e6e23a"/>
          <stop offset="0.35" stop-color="#8cc36c"/>
          <stop offset="0.65" stop-color="#f1ec7a"/>
          <stop offset="0.9" stop-color="#dcdcd6"/>
          <stop offset="1" stop-color="#ececec"/>
        </linearGradient>
      </defs>

      <g class="panel panel--lid">
        <rect width="860" height="640" fill="url(#citrus-swirl)"
              role="img" aria-label="Painted swirl of lemon yellow and leaf green citrus brushstrokes with small spice dots around the label"/>
        <ellipse class="label-oval" cx="440" cy="320" rx="370" ry="250"
                 transform="rotate(-8 440 320)" fill="var(--lid-white)"/>
      </g>

      <g class="panel panel--front">
        <rect y="640" width="860" height="200" fill="url(#side-swirl)"
              role="img" aria-label="Front side wrapped in the same yellow and green citrus brushstrokes"/>
        <line x1="0" y1="640" x2="860" y2="640" stroke="var(--fold-line)" stroke-width="2"/>
      </g>

      <g class="panel panel--side">
        <rect x="860" width="140" height="640" fill="url(#side-swirl)"
              role="img" aria-label="End side wrapped in the same yellow and green citrus brushstrokes"/>
        <line x1="860" y1="0" x2="860" y2="640" stroke="var(--fold-line)" stroke-width="2"/>
      </g>
    </svg>

    <div class="lid-type">
      <div class="brand"><span class="brand__dot"></span>MIRVEL</div>
      <h1 class="product-name">SOAP</h1>
      <span class="product-weight">4oz</span>
    </div>
  </section>
</body>
</html>
```